Wine label Design

We are looking to develop an elegant contemporary Chilean design; for a new Wine Brand TORVANE to be sold in Chinese Market.
We would like to see designs that are a fine balance between having a traditional design that can offer quality reassurance and being distinctive enough to stand out on crowded shelves. The final design should be easy-to-remember and communicate Quality, Tradition and have a conection with Chile.

Target Market(s)

Urban Chinese between 25 to 40 yo

Requirements
Must have
• Paper label
Information on Front label : Grape (example Cabernet sauvignon) / Vintage (ex 2010) / Wine of Chile
Bottle shape is given (see attached)
Nice to have
• An element of uniqueness, easy to recall the brand
Red and Gold Color are appreciated by the Target
Should not have
• White background
Number 4 is considered death, should not be included on the design

```html
<!DOCTYPE html>
<html lang="en">
<head>
<meta charset="utf-8">
<title>TORVANE – Cabernet Sauvignon 2010 Label</title>
<link rel="stylesheet" href="https://fonts.googleapis.com/css2?family=Cinzel:wght@400;600&family=Tinos&display=swap">
<style>
  :root {
    --backdrop: #1d1517;
    --label-paper: #ececeb;
    --wine-red: #a8192a;
    --wine-red-deep: #7c0f1c;
    --gold-light: #f3d9a0;
    --gold-mid: #c9964a;
    --gold-dark: #8a5a22;
    --ink: #2b2325;
  }
  * { margin: 0; padding: 0; box-sizing: border-box; }
  html, body {
    width: 848px;
    height: 1200px;
    overflow: hidden;
    background: var(--backdrop);
  }
  .canvas {
    position: relative;
    width: 848px;
    height: 1200px;
  }
  .label-shape {
    position: absolute;
    inset: 0;
  }
  .brand-name {
    position: absolute;
    top: 355px;
    left: 0;
    width: 848px;
    text-align: center;
    font-family: "Cinzel", serif;
    font-weight: 600;
    font-size: 84px;
    letter-spacing: 8px;
    color: var(--wine-red);
  }
  .grape {
    position: absolute;
    top: 665px;
    left: 330px;
    width: 390px;
    text-align: right;
    font-family: "Tinos", serif;
    font-size: 34px;
    color: var(--ink);
  }
  .vintage {
    position: absolute;
    top: 718px;
    left: 330px;
    width: 390px;
    text-align: right;
    font-family: "Tinos", serif;
    font-size: 30px;
    letter-spacing: 8px;
    color: var(--ink);
  }
  .origin {
    position: absolute;
    top: 818px;
    left: 390px;
    font-family: "Cinzel", serif;
    font-weight: 400;
    font-size: 26px;
    letter-spacing: 1px;
    color: var(--wine-red);
  }
</style>
</head>
<body>
<main class="canvas">
  <svg class="label-shape" width="848" height="1200" viewBox="0 0 848 1200">
    <defs>
      <linearGradient id="gold-band" x1="0" y1="0" x2="1" y2="0">
        <stop offset="0" stop-color="var(--gold-dark)"/>
        <stop offset="0.35" stop-color="var(--gold-light)"/>
        <stop offset="0.65" stop-color="var(--gold-mid)"/>
        <stop offset="1" stop-color="var(--gold-dark)"/>
      </linearGradient>
      <linearGradient id="emblem-fill" x1="0" y1="0" x2="1" y2="1">
        <stop offset="0" stop-color="var(--wine-red)"/>
        <stop offset="1" stop-color="var(--wine-red-deep)"/>
      </linearGradient>
    </defs>

    <path class="label-paper" d="M60 250 Q424 160 788 250 L788 1040 Q424 1130 60 1040 Z" fill="var(--label-paper)"/>

    <path class="gold-band-top" d="M60 250 Q424 160 788 250" fill="none" stroke="url(#gold-band)" stroke-width="16"/>
    <path class="gold-rule-top" d="M60 268 Q424 178 788 268" fill="none" stroke="var(--gold-mid)" stroke-width="2"/>

    <path class="gold-band-bottom" d="M60 1040 Q424 1130 788 1040" fill="none" stroke="url(#gold-band)" stroke-width="16"/>
    <path class="gold-rule-bottom" d="M60 1022 Q424 1112 788 1022" fill="none" stroke="var(--gold-mid)" stroke-width="2"/>

    <line class="name-rule" x1="250" y1="500" x2="598" y2="500" stroke="var(--wine-red)" stroke-width="2"/>
    <rect class="name-ornament" role="img" aria-label="Small red scroll ornament" x="380" y="486" width="88" height="30" rx="10" fill="var(--wine-red)"/>

    <rect class="emblem-illustration" role="img" aria-label="Red illustration of an Easter Island moai statue in profile" x="80" y="690" width="220" height="330" rx="24" fill="url(#emblem-fill)"/>
  </svg>

  <h1 class="brand-name">TORVANE</h1>
  <p class="grape">Cabernet sauvignon</p>
  <p class="vintage">2010</p>
  <p class="origin">WINE OF CHILE</p>
</main>
</body>
</html>
```